Roofing Company Modern look

I want a modern and sophisticated look for our roofing business.

Our address is :

4276 Pellman Crossing Rd
Cedar Hollow, Fl 34791

(407)-583-2716

www.SummitcrestShinglesFl.com

I also want to make sure on the back there is a spot to put
Project Manager Name :

Number:

Because the cards will be used by all sales people

Project Manager Name :

Also there are accreditation we have logos are uploaded here as well that I would like maybe on the back of card as well

I also want to highlight our special attributions or trades:

Residential & Commercial
Fully Insured
License # CCC4872196
Insurance Claims
Serving Central Florida Since 1992
Free Estimates

Contact Information for Business Card

Our address is :

4276 Pellman Crossing Rd
Cedar Hollow, Fl 34791

(407)-583-2716

Project Manager Name :

Residential & Commercial
Fully Insured
License # CCC4872196
Insurance Claims
Free Estimates

Font styles to use
Serif
Sans Serif

Colors
3176b5

Requirements
Must have
• Must have royal blue like my logo grey and black are the colors I like

```html
<!DOCTYPE html>
<html lang="en">
<head>
<meta charset="utf-8">
<title>Summitcrest Shingles &amp; Gutters – Business Card</title>
<link rel="stylesheet" href="https://fonts.googleapis.com/css2?family=Source+Sans+3:wght@400;600;700&display=swap">
<style>
  :root {
    --royal: #2560a8;
    --royal-light: #3176b5;
    --map-tone: #2c6bb2;
    --paper: #f4f4f4;
    --ink: #4a4a4a;
    --charcoal: #4b4b4d;
    --white: #ffffff;
    --backdrop: #e4e4e4;
    --badge-grey: #8a8f96;
    --badge-dark: #2e3440;
  }
  * { margin: 0; padding: 0; box-sizing: border-box; }
  html, body { width: 1200px; height: 960px; overflow: hidden; }
  body {
    background: var(--backdrop);
    font-family: "Source Sans 3", Arial, sans-serif;
    position: relative;
  }
  .card { position: absolute; left: 307px; width: 593px; height: 338px; overflow: hidden; }

  /* Front */
  .card-front { top: 127px; background: var(--royal); color: var(--white); }
  .state-map {
    position: absolute; left: 180px; top: 0; width: 413px; height: 338px;
    background: radial-gradient(ellipse at 75% 35%, var(--map-tone) 0%, var(--royal) 70%);
  }
  .front-brand { position: absolute; left: 0; top: 52px; width: 593px; text-align: center; }
  .brand-mark { width: 62px; height: 62px; border-radius: 50%; background: var(--white); margin: 0 auto 58px; }
  .brand-name {
    font-weight: 600; font-size: 36px; letter-spacing: 2px; line-height: 1;
    text-transform: uppercase;
  }
  .brand-sub {
    font-weight: 600; font-size: 13px; letter-spacing: 2.2px; margin-top: 4px;
    text-transform: uppercase;
  }
  .front-services { position: absolute; left: 0; top: 256px; width: 593px; text-align: center; line-height: 20px; }
  .services-rule { display: flex; align-items: center; justify-content: center; gap: 8px; font-weight: 600; font-size: 14px; }
  .services-rule::before, .services-rule::after { content: ""; width: 106px; height: 1.5px; background: var(--white); }
  .services-list { font-size: 14.5px; }
  .services-since { font-weight: 700; font-size: 14.5px; }

  /* Back */
  .card-back { top: 518px; background: var(--paper); }
  .back-brand { position: absolute; left: 40px; top: 60px; width: 236px; text-align: center; color: var(--royal-light); }
  .back-brand .brand-mark { background: var(--royal-light); margin-bottom: 38px; }
  .back-brand .brand-name { font-size: 27px; letter-spacing: 1.5px; }
  .back-brand .brand-sub { font-size: 10px; letter-spacing: 1.6px; color: var(--royal-light); }
  .badge { position: absolute; }
  .badge-roofer { left: 63px; top: 248px; width: 88px; height: 24px; background: var(--badge-grey); }
  .badge-listing { left: 163px; top: 235px; width: 30px; height: 49px; background: var(--royal-light); border-radius: 3px; }
  .badge-applicator { left: 204px; top: 238px; width: 52px; height: 44px; background: var(--badge-dark); border-radius: 4px; }

  .contact { position: absolute; left: 314px; top: 71px; color: var(--ink); font-size: 15px; line-height: 20px; }
  .contact-name { color: var(--royal); font-weight: 700; font-size: 20px; letter-spacing: 0.3px; line-height: 24px; }
  .contact-title { margin-top: 1px; }
  .contact-rule { width: 28px; height: 2px; background: var(--charcoal); margin: 14px 0 15px; }
  .contact-address { margin-bottom: 8px; }
  .contact-line { display: flex; align-items: center; gap: 6px; }
  .contact-line svg { width: 13px; height: 13px; flex: none; fill: var(--royal); }
  .contact-license { margin-top: 5px; }

  .band-dark { position: absolute; left: 0; bottom: 0; width: 310px; height: 13px; background: var(--charcoal); }
  .band-web {
    position: absolute; right: 0; bottom: 0; width: 290px; height: 29px; background: var(--royal);
    clip-path: polygon(28px 0, 100% 0, 100% 100%, 0 100%);
    color: var(--white); font-size: 15px; line-height: 29px; padding-left: 56px;
  }
</style>
</head>
<body>

<section class="card card-front">
  <div class="state-map" role="img" aria-label="Faint map of the state of Florida"></div>
  <div class="front-brand">
    <div class="brand-mark"></div>
    <div class="brand-name">Summitcrest</div>
    <div class="brand-sub">Shingles &amp; Gutters Inc.</div>
  </div>
  <div class="front-services">
    <div class="services-rule">RESIDENTIAL &amp; COMMERCIAL</div>
    <div class="services-list">Fully Insured • Insurance Claims • Free Estimates</div>
    <div class="services-since">Serving Central Florida Since 1992</div>
  </div>
</section>

<section class="card card-back">
  <div class="back-brand">
    <div class="brand-mark"></div>
    <div class="brand-name">Summitcrest</div>
    <div class="brand-sub">Shingles &amp; Gutters Inc.</div>
  </div>
  <div class="badge badge-roofer" role="img" aria-label="Roofing contractor accreditation badge"></div>
  <div class="badge badge-listing" role="img" aria-label="Business accreditation badge"></div>
  <div class="badge badge-applicator" role="img" aria-label="Shingle applicator certification badge"></div>

  <div class="contact">
    <div class="contact-name">DANIEL WHITAKER</div>
    <div class="contact-title">Project Manager</div>
    <div class="contact-rule"></div>
    <div class="contact-address">4276 Pellman Crossing Rd<br>Cedar Hollow, Fl 34791</div>
    <div class="contact-line">
      <svg viewBox="0 0 13 13"><path d="M3 0h7a1 1 0 0 1 1 1v11a1 1 0 0 1-1 1H3a1 1 0 0 1-1-1V1a1 1 0 0 1 1-1zm.5 1.5v8.5h6V1.5z"/></svg>
      (407) 583-2716
    </div>
    <div class="contact-line">
      <svg viewBox="0 0 13 13"><path d="M2.6 0.5l2 2.3c.3.4.3.9 0 1.2L3.7 5c.9 1.8 2.4 3.3 4.3 4.3l1-.9c.3-.3.9-.3 1.2 0l2.3 2c.4.3.4.9 0 1.2l-1.2 1.1C9.5 14 0 5.1.9 2.1L2 .6c.2-.4.3-.3.6-.1z"/></svg>
      (407) 583-2716
    </div>
    <div class="contact-line">
      <svg viewBox="0 0 13 13"><path d="M0 2.5h13v8H0zm1.4 1l5.1 3.6 5.1-3.6zm-.4 1v5h11v-5L6.5 8.3z"/></svg>
      daniel@SummitcrestShinglesFl.com
    </div>
    <div class="contact-license">License # CCC4872196</div>
  </div>

  <div class="band-dark"></div>
  <div class="band-web">www.SummitcrestShinglesFl.com</div>
</section>

</body>
</html>
```